Vector Images for Data Collection Process

We are an Australian based company that offer psychometric solutions and we require three separate related vector images to represent our data collection process for use on marketing material and our website. The images are to be designed incorporating but not limited to our corporate colors and also a version in grey scale. We require versions in JPG, PNG and AI formats.

Reason: Hi all, We have extended the deadline for this contest to allow designers to review feedback and make alterations if necessary. Thanks Joyce

Industry/Entity Type

It Company

Other font styles liked:
• Myriad Pro

Requirements
Must have
• The three separate vector images are related as a continuation of the process but also able to be used individually. The image should relate to the content which is below the sample images provided in the attachment titled Data Vector and should come in a version of the graphic by itself and also with the heading (either Collect, Discover or Collect) and the related content underneath. The text content under the heading is not to be altered.

```html
<!DOCTYPE html>
<html lang="en">
<head>
<meta charset="utf-8">
<title>Collect – Data Process</title>
<link rel="stylesheet" href="https://fonts.googleapis.com/css2?family=Source+Sans+3:wght@400;600;700&display=swap">
<style>
  :root {
    --blue: #0a86cf;
    --line-blue: #1a8ad4;
    --green: #7ab800;
    --ink: #000000;
    --paper: #ffffff;
  }
  html, body {
    margin: 0;
    padding: 0;
    overflow: hidden;
    background: var(--paper);
  }
  .canvas {
    position: relative;
    width: 1200px;
    height: 800px;
    overflow: hidden;
    background: var(--paper);
    font-family: "Source Sans 3", "Myriad Pro", sans-serif;
    color: var(--ink);
  }
  .data-graphic {
    position: absolute;
    left: 0;
    top: 0;
    width: 1200px;
    height: 800px;
  }
  .hub-label {
    font-family: "Source Sans 3", sans-serif;
    font-weight: 700;
    font-size: 40px;
    fill: var(--ink);
  }
  .connector { fill: none; stroke: var(--line-blue); stroke-width: 1.6; }
  .outer-ring { fill: none; stroke: var(--line-blue); stroke-width: 1.6; }
  .ring-green { fill: none; stroke: var(--green); stroke-width: 9; }
  .ring-blue { fill: none; stroke: var(--blue); stroke-width: 9; }
  .icon-blue { fill: var(--blue); }
  .icon-green { fill: var(--green); }
  .step-copy {
    position: absolute;
    left: 0;
    top: 454px;
    width: 1200px;
    text-align: center;
  }
  .step-title {
    margin: 0;
    font-weight: 700;
    font-size: 30px;
    line-height: 36px;
    letter-spacing: 0.2px;
  }
  .step-text {
    margin: 6px auto 0;
    font-size: 22px;
    line-height: 27.2px;
  }
  .step-line { display: block; white-space: nowrap; }
</style>
</head>
<body>
<div class="canvas">
  <svg class="data-graphic" viewBox="0 0 1500 1000" aria-hidden="true">
    <circle class="outer-ring" cx="742" cy="390" r="105" pathLength="360" stroke-dasharray="37 8" stroke-dashoffset="-4"/>
    <circle class="ring-green" cx="742" cy="390" r="62" pathLength="360" stroke-dasharray="35 55" stroke-dashoffset="-50" transform="rotate(-90 742 390)"/>
    <circle class="ring-blue" cx="742" cy="390" r="62" pathLength="360" stroke-dasharray="35 55" stroke-dashoffset="-5" transform="rotate(-90 742 390)"/>
    <text class="hub-label" x="742" y="404" text-anchor="middle">DATA</text>

    <path class="connector" d="M732 287 V255"/>
    <path class="connector" d="M808 308 L830 287 H900"/>
    <path class="connector" d="M846 379 H878"/>
    <path class="connector" d="M823 455 L845 478 H915"/>
    <path class="connector" d="M752 493 V525"/>
    <path class="connector" d="M677 470 L655 493 H585"/>
    <path class="connector" d="M640 400 H608"/>
    <path class="connector" d="M662 325 L640 302 H570"/>

    <g class="icon-pie">
      <path class="icon-green" d="M733 217 A17 17 0 1 0 750 234 L733 234 Z"/>
      <path class="icon-green" d="M737 213 A17 17 0 0 1 754 230 L737 230 Z"/>
    </g>
    <g class="icon-board">
      <rect class="icon-green" x="904" y="270" width="36" height="24"/>
      <polyline points="910,288 917,281 923,285 933,276" fill="none" stroke="var(--blue)" stroke-width="2"/>
      <path d="M917 294 L913 304 M927 294 L931 304 M922 266 V270" stroke="var(--green)" stroke-width="2.5"/>
    </g>
    <g class="icon-bars">
      <rect class="icon-blue" x="885" y="372" width="7" height="22"/>
      <rect class="icon-blue" x="895" y="383" width="6" height="11"/>
      <rect class="icon-blue" x="904" y="360" width="6" height="34"/>
      <rect class="icon-blue" x="913" y="345" width="7" height="49"/>
    </g>
    <g class="icon-folder">
      <path class="icon-green" d="M920 485 H934 L937 489 H951 V510 H920 Z"/>
      <path class="icon-blue" d="M914 482 H926 L929 486 H944 V510 H914 Z"/>
    </g>
    <g class="icon-dollar">
      <text x="765" y="540" text-anchor="middle" font-family="Source Sans 3, sans-serif" font-weight="700" font-size="24" fill="var(--green)">$</text>
      <path d="M748 541 A16 12 0 0 0 778 545" fill="none" stroke="var(--green)" stroke-width="3"/>
      <path class="icon-green" d="M744 534 L752 538 L745 545 Z"/>
    </g>
    <g class="icon-bulb">
      <circle class="icon-blue" cx="585" cy="518" r="11"/>
      <rect class="icon-blue" x="579" y="526" width="12" height="12" rx="2"/>
      <path d="M580 532 H590 M580 535 H590" stroke="#fff" stroke-width="1"/>
      <path d="M585 495 V502 M570 503 L575 508 M600 503 L595 508" stroke="var(--blue)" stroke-width="2.5"/>
      <path d="M585 512 V522" stroke="#fff" stroke-width="1.5"/>
    </g>
    <g class="icon-thumb">
      <rect class="icon-green" x="559" y="389" width="11" height="17"/>
      <path d="M573 390 L582 380 L584 372 C590 372 591 378 589 386 H596 C599 386 599 392 596 393 C599 395 598 399 595 400 C597 402 595 406 592 406 H573 Z" fill="none" stroke="var(--green)" stroke-width="2.5"/>
    </g>
    <g class="icon-people">
      <circle class="icon-blue" cx="561" cy="265" r="7"/>
      <path class="icon-blue" d="M549 292 C549 276 573 276 573 292 Z"/>
      <circle class="icon-blue" cx="577" cy="272" r="5.5"/>
      <path class="icon-blue" d="M567 293 C567 280 587 280 587 293 Z"/>
      <circle class="icon-blue" cx="594" cy="277" r="4.5"/>
      <path class="icon-blue" d="M586 293 C586 283 601 283 601 293 Z"/>
    </g>
  </svg>

  <section class="step-copy">
    <h1 class="step-title">COLLECT</h1>
    <p class="step-text">
      <span class="step-line">We collect a range of people data</span>
      <span class="step-line">including demogrpahic</span>
      <span class="step-line">information, assessment results</span>
      <span class="step-line">and outcome data on successful</span>
      <span class="step-line">and unsuccessful candidates</span>
    </p>
  </section>
</div>
</body>
</html>
```